Brivolan - presentation for a remote DBA team offering data platform management

We need a website design for wordpress site called Brivolan.cz
We deliver remote database and data platform administration and development, oversee the database administrators, consult and train the personnel responsible for the database operations. The website should include several sections, home page with graphics elements supporting the name and service - remote dba work; blog section; service introduction and description, team introduction and description, download section for documents, presentations etc.

Target Market(s)

small and medium business companies requiring remote DBA service

Number of Pages Required

3 page

Font styles to use
Sans Serif

Colors

Designer to choose colors to be used in the design.

Requirements
Must have
• The website should have several sections to introduce the services, blog, team introduction, downloads

```html
<!DOCTYPE html>
<html lang="en">
<head>
<meta charset="utf-8">
<title>Brivolan – Data Platform Management</title>
<link href="https://fonts.googleapis.com/css2?family=Nunito:wght@300;400;600;700&family=Montserrat:wght@400;500;600;700&display=swap" rel="stylesheet">
<style>
:root{
  --blue:#0b7fe8;
  --blue-deep:#0566c9;
  --blue-light:#2f97f2;
  --ink:#2d3338;
  --muted:#8d959c;
  --soft:#eceff2;
  --line:#d5dadf;
  --white:#ffffff;
  --dark:#1c1e20;
  --dark-line:#35383b;
}
*{box-sizing:border-box;margin:0;padding:0}
html,body{width:1200px;height:2830px;overflow:hidden}
body{font-family:"Montserrat",sans-serif;color:var(--ink);background:var(--white)}
.page{position:relative;width:1200px;height:2830px}
.wrap{position:relative;width:760px;margin:0 auto}
.h-section{font-family:"Nunito",sans-serif;font-weight:300;font-size:34px;line-height:44px;text-align:center;color:#4b5257}
.h-rule{width:170px;height:1px;background:var(--line);margin:14px auto 0}
.chev{position:absolute;left:50%;width:34px;height:34px;margin-left:-17px;border-radius:50%;background:var(--white);display:flex;align-items:center;justify-content:center;z-index:2}
.chev.on-soft{background:var(--soft)}

/* hero */
.hero{position:relative;height:420px;color:var(--white);overflow:hidden}
.hero-bg{position:absolute;inset:0;background:radial-gradient(ellipse at 30% 40%,#2b95f5 0%,#0b7fe8 45%,#0a6fd6 100%)}
.topbar{display:flex;justify-content:space-between;align-items:flex-start;padding-top:30px}
.logo-name{font-weight:700;font-size:24px;letter-spacing:.5px;line-height:1}
.logo-sub{font-size:9.5px;font-weight:500;margin-top:5px;letter-spacing:.3px}
.nav{display:flex;flex-direction:column;align-items:flex-end}
.btn-outline{border:1.5px solid var(--white);color:var(--white);font-size:9.5px;font-weight:600;letter-spacing:.5px;padding:4px 14px;border-radius:2px;display:inline-block}
.nav ul{list-style:none;display:flex;gap:20px;margin-top:12px;font-size:9.5px;font-weight:600}
.nav li.current{opacity:.7;font-weight:500}
.hero-copy{text-align:center;margin-top:72px}
.hero-title{font-family:"Nunito",sans-serif;font-size:27px;font-weight:400}
.hero-title b{font-weight:700;letter-spacing:.3px}
.hero-text{width:560px;margin:14px auto 0;font-size:11px;line-height:18px;font-family:"Nunito",sans-serif}
.hero-copy .btn-outline{margin-top:26px;padding:10px 22px;font-size:10px}
.hero .chev{bottom:-17px}

/* why */
.why{position:relative;height:300px;padding-top:46px}
.features{display:flex;justify-content:space-between;width:670px;margin:28px auto 0}
.feature{width:190px;text-align:center}
.feature svg{display:block;margin:0 auto}
.feature h3{font-size:12px;font-weight:500;margin-top:14px;color:#3a4045}
.feature p{font-family:"Nunito",sans-serif;font-size:10px;line-height:16px;color:#a1a8ae;margin-top:8px}
.why .small-chev{position:absolute;left:50%;bottom:8px;margin-left:-7px}

/* clients */
.clients{position:relative;height:275px;padding-top:18px}
.client-row{display:flex;justify-content:space-between;align-items:center;width:700px;margin:30px auto 0;height:60px}
.client{font-family:"Montserrat",sans-serif;font-size:22px;font-weight:600;color:#3b3f43;display:flex;align-items:center;gap:8px}
.client .mark{width:12px;height:12px;background:#3b3f43;border-radius:50%}
.client.light{color:#8b9196}
.carousel{display:flex;justify-content:center;align-items:center;gap:14px;margin-top:32px}
.arrow{width:26px;height:26px;border-radius:50%;background:#eef2f6;display:flex;align-items:center;justify-content:center}
.dots{display:flex;gap:9px;align-items:center}
.dots span{width:5px;height:5px;border-radius:50%;background:#3a3f44}
.dots span.on{width:9px;height:9px;background:var(--blue)}

/* services */
.services{position:relative;height:465px;background:var(--soft);padding-top:48px}
.services .h-section{font-size:32px;color:#555c62}
.services .lead{width:390px;margin:28px auto 0;text-align:center;font-family:"Nunito",sans-serif;font-size:11px;line-height:18px;color:#6f777d}
.cards{display:flex;gap:4px;width:752px;margin:40px auto 0}
.card{width:185px;height:190px;background:var(--white);border-bottom:5px solid #9ea4a9;text-align:center;padding-top:30px}
.card .ring{width:82px;height:82px;border:1.5px solid var(--blue);border-radius:50%;margin:0 auto;display:flex;align-items:center;justify-content:center}
.card h4{font-size:11px;font-weight:700;margin-top:26px;line-height:14px;color:#24292d}
.services .chev{bottom:-17px}

/* team */
.team{position:relative;height:445px;padding-top:40px}
.team .lead{width:700px;margin:20px auto 0;text-align:center;font-family:"Nunito",sans-serif;font-size:14px;line-height:22px;color:#3e454a}
.members{display:flex;gap:12px;width:696px;margin:24px auto 0;justify-content:center}
.member{width:165px;text-align:center}
.portrait{width:165px;height:186px}
.member h5{font-size:10px;line-height:13px;font-weight:700;margin-top:14px}
.member p{font-size:8px;line-height:11px;color:var(--muted);margin-top:3px;font-family:"Nunito",sans-serif}

/* download */
.download{position:relative;height:195px;background:var(--blue);color:var(--white);text-align:center;padding-top:28px}
.download h2{font-family:"Nunito",sans-serif;font-weight:400;font-size:31px;color:#62c7ff}
.download p{font-size:11.5px;font-weight:500;margin-top:26px;font-family:"Nunito",sans-serif}
.download .btn-outline{margin-top:18px;padding:11px 16px;font-size:10px;border-radius:3px}
.download .chev{bottom:-17px}

/* news */
.news{position:relative;height:460px;background:var(--soft);padding-top:40px}
.news .lead{width:430px;margin:22px auto 0;text-align:center;font-family:"Nunito",sans-serif;font-size:11px;line-height:18px;color:#5f676d}
.posts{display:flex;gap:24px;width:690px;margin:28px auto 0}
.post{width:214px;height:262px;background:var(--white);box-shadow:0 2px 6px rgba(0,0,0,.06)}
.post-image{width:214px;height:137px}
.post-meta{font-size:8px;color:var(--muted);padding:16px 15px 0;display:flex;gap:6px;align-items:center;font-family:"Nunito",sans-serif}
.post h6{font-family:"Nunito",sans-serif;font-weight:400;font-size:13px;line-height:19px;padding:12px 15px 0;color:#2c3136}

/* footer */
.footer{height:270px;background:var(--dark);color:var(--white);padding-top:48px}
.footer-top{display:flex;width:752px;margin:0 auto}
.footer-brand{width:155px}
.footer-brand .logo-name{font-size:17px}
.footer-brand .logo-sub{font-size:7.5px;margin-top:3px}
.footer-contact{width:225px;border-left:1px solid var(--dark-line);border-right:1px solid var(--dark-line);padding-left:36px;height:150px}
.contact-line{display:flex;align-items:center;gap:12px;font-size:9px;margin-bottom:16px}
.signup-label{font-size:9px;color:#5e6367;letter-spacing:.5px;margin-bottom:6px}
.field{width:128px;height:22px;background:var(--white);color:#777;font-size:8.5px;padding:5px 7px}
.submit{width:128px;height:20px;background:var(--blue);font-size:10px;font-weight:700;text-align:center;line-height:20px;margin-top:6px}
.footer-links{flex:1;padding-left:36px}
.footer-links ul{list-style:none;display:flex;justify-content:space-between;font-size:10px;font-weight:500}
.footer-row{display:flex;justify-content:space-between;align-items:center;margin-top:28px}
.btn-solid{background:var(--blue);font-size:8.5px;font-weight:700;padding:5px 14px;letter-spacing:.3px}
.social{display:flex;gap:7px}
.social span{width:22px;height:22px;border-radius:50%;background:var(--blue)}
.footer-bottom{width:752px;margin:22px auto 0;border-top:1px solid var(--dark-line);padding-top:16px;font-size:7.5px;color:#8b9094;display:flex;gap:10px}
</style>
</head>
<body>
<div class="page">

<header class="hero">
  <div class="hero-bg" role="img" aria-label="Blue background with a faint pattern of gears and a human profile suggesting remote data work"></div>
  <div class="wrap">
    <div class="topbar">
      <div class="logo">
        <div class="logo-name">BRIVOLAN</div>
        <div class="logo-sub">COMPLETE DATA SOLUTION</div>
      </div>
      <nav class="nav">
        <span class="btn-outline">REQUEST A DEMO</span>
        <ul>
          <li class="current">PRODUCTS</li>
          <li>SOLUTIONS</li>
          <li>WHY BRIVOLAN</li>
          <li>RESOURCES</li>
          <li>ABOUT BRIVOLAN</li>
        </ul>
      </nav>
    </div>
    <div class="hero-copy">
      <h1 class="hero-title">DBA team offering <b>DATA PLATFORM MANAGEMENT</b></h1>
      <p class="hero-text">Lorem Ipsum is simply dummy text of the printing and typesetting industry. Lorem Ipsum has been the industry's standard dummy text ever since the 1500s Lorem Ipsum is simply dummy text &nbsp;Lorem Ipsum is simply dummy text of the printing and typesetting industry.</p>
      <span class="btn-outline">EXPLORE</span>
    </div>
  </div>
  <div class="chev"><svg width="12" height="8" viewBox="0 0 12 8"><path d="M1 1l5 5 5-5" fill="none" stroke="#0b7fe8" stroke-width="1.6"/></svg></div>
</header>

<section class="why">
  <h2 class="h-section">Why Choose Ours</h2>
  <div class="h-rule"></div>
  <div class="features">
    <div class="feature">
      <svg width="44" height="44" viewBox="0 0 44 44"><circle cx="22" cy="22" r="16" fill="#e3f0fc"/><circle cx="22" cy="22" r="12" fill="none" stroke="#0b7fe8" stroke-width="1.6"/><circle cx="22" cy="22" r="8" fill="none" stroke="#0b7fe8" stroke-width="1"/><path d="M18 22l3 3 5-6" fill="none" stroke="#0b7fe8" stroke-width="1.6"/></svg>
      <h3>100% Uptime Guarantee</h3>
      <p>Even the all-powerful Pointing has no control about the blind texts it is an almost unorthographic.</p>
    </div>
    <div class="feature">
      <svg width="44" height="44" viewBox="0 0 44 44"><circle cx="24" cy="26" r="14" fill="#e3f0fc"/><path d="M22 8l11 4v9c0 8-5 13-11 15-6-2-11-7-11-15v-9z" fill="none" stroke="#0b7fe8" stroke-width="1.6"/><circle cx="22" cy="22" r="5" fill="none" stroke="#0b7fe8" stroke-width="1.4"/></svg>
      <h3>Safe and Secured</h3>
      <p>Even the all-powerful Pointing has no control about the blind texts it is an almost unorthographic.</p>
    </div>
    <div class="feature">
      <svg width="44" height="44" viewBox="0 0 44 44"><circle cx="24" cy="28" r="13" fill="#e3f0fc"/><circle cx="22" cy="17" r="7" fill="none" stroke="#0b7fe8" stroke-width="1.6"/><path d="M10 36c1-7 6-10 12-10s11 3 12 10" fill="none" stroke="#0b7fe8" stroke-width="1.6"/><path d="M14 17a8 8 0 0 1 16 0" fill="none" stroke="#0b7fe8" stroke-width="1.6"/></svg>
      <h3>Our Dedicated Support</h3>
      <p>Even the all-powerful Pointing has no control about the blind texts it is an almost unorthographic.</p>
    </div>
  </div>
  <svg class="small-chev" width="14" height="9" viewBox="0 0 14 9"><path d="M1 1l6 6 6-6" fill="none" stroke="#b9c0c6" stroke-width="1.4"/></svg>
</section>

<section class="clients">
  <h2 class="h-section">Some of Our Clients</h2>
  <div class="h-rule"></div>
  <div class="client-row">
    <div class="client"><span class="mark"></span>Norvale</div>
    <div class="client light">ostrellia</div>
    <div class="client">kestro</div>
    <div class="client">Halden &amp; Pike</div>
  </div>
  <div class="carousel">
    <div class="arrow"><svg width="8" height="12" viewBox="0 0 8 12"><path d="M7 1L2 6l5 5" fill="none" stroke="#0b7fe8" stroke-width="1.6"/></svg></div>
    <div class="dots"><span></span><span></span><span></span><span class="on"></span><span></span><span></span></div>
    <div class="arrow"><svg width="8" height="12" viewBox="0 0 8 12"><path d="M1 1l5 5-5 5" fill="none" stroke="#0b7fe8" stroke-width="1.6"/></svg></div>
  </div>
</section>

<section class="services">
  <h2 class="h-section">DBA team offering data platform management</h2>
  <p class="lead">Lorem Ipsum is simply dummy text of the printing and typesetting industry. Lorem Ipsum has been the industry's standard dummy text ever since the 1500s, when an unknown printer took a galley of type and scrambled it to make a type specimen book.</p>
  <div class="cards">
    <div class="card">
      <div class="ring"><svg width="42" height="42" viewBox="0 0 42 42"><rect x="5" y="8" width="32" height="22" rx="2" fill="none" stroke="#0b7fe8" stroke-width="1.6"/><path d="M10 24l6-6 5 4 7-8" fill="none" stroke="#0b7fe8" stroke-width="1.6"/><path d="M15 35h12M21 30v5" stroke="#0b7fe8" stroke-width="1.6"/></svg></div>
      <h4>DATA MANAGEMENT<br>PLATFORM</h4>
    </div>
    <div class="card">
      <div class="ring"><svg width="42" height="42" viewBox="0 0 42 42"><rect x="7" y="7" width="28" height="28" rx="2" fill="none" stroke="#0b7fe8" stroke-width="1.6"/><circle cx="21" cy="21" r="6" fill="none" stroke="#0b7fe8" stroke-width="1.6"/><path d="M21 11v4M21 27v4M11 21h4M27 21h4" stroke="#0b7fe8" stroke-width="1.6"/></svg></div>
      <h4>DATA EXCHANGE</h4>
    </div>
    <div class="card">
      <div class="ring"><svg width="42" height="42" viewBox="0 0 42 42"><rect x="6" y="8" width="30" height="20" rx="2" fill="none" stroke="#0b7fe8" stroke-width="1.6"/><circle cx="21" cy="18" r="5" fill="none" stroke="#0b7fe8" stroke-width="1.4"/><path d="M14 34h14M21 28v6" stroke="#0b7fe8" stroke-width="1.6"/></svg></div>
      <h4>CROSS-DEVICE</h4>
    </div>
    <div class="card">
      <div class="ring"><svg width="42" height="42" viewBox="0 0 42 42"><rect x="6" y="7" width="30" height="24" rx="2" fill="none" stroke="#0b7fe8" stroke-width="1.6"/><circle cx="25" cy="21" r="6" fill="none" stroke="#0b7fe8" stroke-width="1.4"/><path d="M25 15v6h6" fill="none" stroke="#0b7fe8" stroke-width="1.4"/><path d="M10 13h8M10 18h6M10 23h6" stroke="#0b7fe8" stroke-width="1.4"/></svg></div>
      <h4>AUDIENCE OPTIMIZER</h4>
    </div>
  </div>
  <div class="chev on-soft"><svg width="12" height="8" viewBox="0 0 12 8"><path d="M1 1l5 5 5-5" fill="none" stroke="#b9c0c6" stroke-width="1.6"/></svg></div>
</section>

<section class="team">
  <h2 class="h-section">Our Team</h2>
  <div class="h-rule"></div>
  <p class="lead">Want to know what's new at Brivolan? Or just looking for more information about how some marketers, agencies, and publishers have used Brivolan to meet their business goals?</p>
  <div class="members">
    <div class="member">
      <div class="portrait" role="img" aria-label="Portrait photo of Tomas Verlin in a red shirt" style="background:linear-gradient(180deg,#e9ecef 0%,#d84a45 70%,#c23a36 100%)"></div>
      <h5>Tomas Verlin</h5><p>Managing Director (Sales)</p>
    </div>
    <div class="member">
      <div class="portrait" role="img" aria-label="Portrait photo of Julian Marsh with a purple scarf" style="background:linear-gradient(180deg,#f1f0ee 0%,#b78f86 55%,#8e4f8c 100%)"></div>
      <h5>Julian Marsh</h5><p>Creative Art Director (Project)</p>
    </div>
    <div class="member">
      <div class="portrait" role="img" aria-label="Portrait photo of Ivo Stranik in a white t-shirt" style="background:linear-gradient(180deg,#8aa6b6 0%,#c7a58e 50%,#eceff1 100%)"></div>
      <h5>Ivo Stranik</h5><p>Senior Core Developer</p>
    </div>
    <div class="member">
      <div class="portrait" role="img" aria-label="Portrait photo of Mira Holt in a patterned top" style="background:linear-gradient(180deg,#9fb3ba 0%,#6e5a52 45%,#d7b3a0 75%,#d86a8a 100%)"></div>
      <h5>Mira Holt</h5><p>Creative Content Developer</p>
    </div>
  </div>
</section>

<section class="download">
  <h2>Our Download</h2>
  <p>Check out the News &amp; Resources section for case studies, whitepapers, news, events, and lots more!</p>
  <span class="btn-outline">DOWNLOAD OUR PRESENTATION</span>
  <div class="chev on-soft"><svg width="12" height="8" viewBox="0 0 12 8"><path d="M1 1l5 5 5-5" fill="none" stroke="#0b7fe8" stroke-width="1.6"/></svg></div>
</section>

<section class="news">
  <h2 class="h-section">News &amp; Resources</h2>
  <div class="h-rule"></div>
  <p class="lead">Lorem Ipsum is simply dummy text of the printing and typesetting industry. Lorem Ipsum has been the industry's standard dummy text ever</p>
  <div class="posts">
    <article class="post">
      <div class="post-image" role="img" aria-label="Desk with a plant, laptop and sketched charts" style="background:linear-gradient(135deg,#6fb7c9 0%,#e8eaec 55%,#d9a36a 100%)"></div>
      <div class="post-meta">August 12, 2018 &nbsp;Admin <svg width="9" height="8" viewBox="0 0 9 8"><rect x=".5" y=".5" width="8" height="5.5" fill="none" stroke="#8d959c"/></svg>3</div>
      <h6>Even the all-powerful Pointing has no control about the blind texts</h6>
    </article>
    <article class="post">
      <div class="post-image" role="img" aria-label="Person holding a blue magazine against a pale background" style="background:linear-gradient(180deg,#dfe9ee 0%,#8fb7d6 55%,#e5e7e8 100%)"></div>
      <div class="post-meta">August 12, 2018 &nbsp;Admin <svg width="9" height="8" viewBox="0 0 9 8"><rect x=".5" y=".5" width="8" height="5.5" fill="none" stroke="#8d959c"/></svg>3</div>
      <h6>Even the all-powerful Pointing has no control about the blind texts</h6>
    </article>
    <article class="post">
      <div class="post-image" role="img" aria-label="Close-up of pink and violet crystals" style="background:linear-gradient(135deg,#f3b8d6 0%,#c9a3e6 50%,#f6d7e4 100%)"></div>
      <div class="post-meta">August 12, 2018 &nbsp;Admin <svg width="9" height="8" viewBox="0 0 9 8"><rect x=".5" y=".5" width="8" height="5.5" fill="none" stroke="#8d959c"/></svg>3</div>
      <h6>Even the all-powerful Pointing has no control about the blind texts</h6>
    </article>
  </div>
</section>

<footer class="footer">
  <div class="footer-top">
    <div class="footer-brand">
      <div class="logo-name">BRIVOLAN</div>
      <div class="logo-sub">COMPLETE DATA SOLUTION</div>
    </div>
    <div class="footer-contact">
      <div class="contact-line"><svg width="12" height="15" viewBox="0 0 12 15"><path d="M6 14S1 8.5 1 5.5a5 5 0 0 1 10 0C11 8.5 6 14 6 14z" fill="none" stroke="#2f97f2" stroke-width="1.4"/><circle cx="6" cy="5.5" r="1.8" fill="#2f97f2"/></svg>See Our Locations</div>
      <div class="contact-line"><svg width="13" height="10" viewBox="0 0 13 10"><rect x=".7" y=".7" width="11.6" height="8.6" fill="none" stroke="#2f97f2" stroke-width="1.3"/><path d="M1 1l5.5 4.5L12 1" fill="none" stroke="#2f97f2" stroke-width="1.3"/></svg>info@brivolan.cz</div>
      <div class="signup-label">NEWSLETTER SIGNUP</div>
      <div class="field">Email Address</div>
      <div class="submit">SUBMIT</div>
    </div>
    <div class="footer-links">
      <ul><li>CONTACT US</li><li>CAREERS</li><li>EVENTS</li><li>AWARDS</li></ul>
      <div class="footer-row">
        <span class="btn-solid">REQUEST A DEMO</span>
        <div class="social"><span></span><span></span><span></span><span></span></div>
      </div>
    </div>
  </div>
  <div class="footer-bottom">
    <span>Copyright ©2018 Brivolan Solutions, Inc.</span><span>|</span><span>Privacy Center</span><span>|</span><span>Opt Out</span><span>|</span><span>Site Map</span>
  </div>
</footer>

</div>
</body>
</html>
```